Website for an electrical contractor :)

We are after a web site which can show pictures of our jobs and our capability in a professional, creative and easily understood way.

----- Brightvale Electrical ------

We really want a visually good looking website with three sections

Section one:
'Completed projects'
We have a few pictures of jobs which we've completed and would like to show off with a brief description. (see uploads)

Section two:
'Our capabilities'
Just a list of what services we offer

Section three:
We would like a 'contact us' section which people can send us a short msg and upload a file for plans to be able to send to us. We would need their name, phone number and email details. We would also need a short privacy policy saying 'we do not disclose information to third parties'.
We also want to display our contact number and postal address

Good luck :)

Target Market(s)

Adults 25 years+
Business owners
Builders
Real estate agents

Industry/Entity Type

Electrical

Colors

Designer to choose colors to be used in the design.

Requirements
Must have
• Visually appealing
Easy to understand
In the 'Completed projects' section, must have a list for each project we do i can upload pictures for it.

```html
<!DOCTYPE html>
<html lang="en">
<head>
<meta charset="utf-8">
<title>Brightvale Electrical</title>
<link href="https://fonts.googleapis.com/css2?family=Alegreya+Sans:ital,wght@0,400;0,700;1,400&family=Open+Sans:wght@300;400&display=swap" rel="stylesheet">
<style>
:root{
  --white:#ffffff;
  --ink:#2b2b2b;
  --body:#4a4a4a;
  --muted:#9a9a9a;
  --topbar:#e2e2e2;
  --section-grey:#efefef;
  --divider:#c4c4c4;
  --band:#4b4b4b;
  --contact-bg:#c9c9c9;
  --panel:#e4e4e4;
  --button:#b5b5b5;
  --accent:#c8202a;
}
*{box-sizing:border-box;margin:0;padding:0}
html,body{width:1200px;height:4200px;overflow:hidden}
body{background:var(--white);font-family:"Alegreya Sans",sans-serif;color:var(--body);position:relative}
.abs{position:absolute}
.center{left:0;width:1200px;text-align:center}

.topbar{top:0;left:0;width:1200px;height:30px;background:var(--topbar);font-size:14px;color:#777;text-align:center;line-height:30px;word-spacing:2px}
.topbar span{margin:0 14px}

.header{top:30px;left:0;width:1200px;height:135px;background:var(--white)}
.brand{left:90px;top:44px;display:flex;align-items:center;gap:14px}
.brand-mark{width:22px;height:22px;background:var(--accent)}
.brand-name{font-size:44px;color:var(--ink);line-height:1}
.nav{top:68px;font-family:"Open Sans",sans-serif;font-size:17px;color:var(--muted);text-transform:uppercase}
.nav.active{color:var(--ink)}

.hero{top:165px;left:0;width:1200px;height:595px;background:linear-gradient(180deg,#3e4246 0%,#6a6c6c 45%,#8a8884 75%,#5d5b58 100%)}
.hero-title{top:300px;font-family:"Open Sans",sans-serif;font-weight:300;font-size:50px;color:var(--white)}
.hero-sub{top:372px;font-family:"Open Sans",sans-serif;font-size:20px;color:#e8e8e8}

.section-title{font-size:48px;color:var(--ink);line-height:1}
.section-title b{font-weight:700}
.section-sub{font-size:31px;font-style:italic;color:#444;line-height:1}
.divider{left:510px;width:180px;height:6px;background:var(--divider)}
.copy{left:285px;width:630px;text-align:center;font-size:18.5px;line-height:24px;color:#3e3e3e}

.works{top:1296px;left:0;width:1200px;height:1248px;background:var(--section-grey)}
.feature{left:105px;top:180px;width:984px;height:504px;background:linear-gradient(180deg,#2a2a2a 0%,#6e6d6a 32%,#b6b3ab 60%,#8b857a 100%)}
.feature-band{left:0;top:189px;width:984px;height:150px;background:rgba(235,235,235,.55)}
.feature-title{left:0;width:984px;top:40px;text-align:center;font-size:38px;color:#333}
.feature-date{left:0;width:984px;top:86px;text-align:center;font-size:30px;font-style:italic;color:#333}
.thumb{top:708px;height:498px}

.notice{top:2544px;left:0;width:1200px;height:96px;background:var(--band);color:var(--white);text-align:center;line-height:96px;font-size:27px}

.cap-head{font-size:34px;color:#333}
.cap-list{list-style:none;font-size:18px;line-height:26.8px;color:#333}
.cap-left{right:618px;text-align:right}
.cap-right{left:624px}
.support{top:3538px;font-size:18px;font-style:italic;letter-spacing:7px;color:#555}

.contact{top:3624px;left:0;width:1200px;height:576px;background:var(--contact-bg)}
.form-panel{left:72px;top:21px;width:528px;height:507px;background:var(--panel)}
.field{left:18px;width:477px;height:48px;background:var(--white);font-size:24px;font-style:italic;color:#555;padding:10px 14px;letter-spacing:1px}
.field small{font-size:14px;color:var(--accent)}
.upload{left:366px;width:147px;height:48px;background:var(--button);font-size:24px;color:#444;text-align:center;line-height:48px}
.send{left:375px;top:444px;width:138px;height:45px;background:var(--button);color:var(--white);text-align:center;line-height:45px;font-size:22px;letter-spacing:2px}
.info{left:630px;width:470px;color:#444}
.info h2{font-size:25px;font-weight:700;color:#333}
.info p{font-size:19px;font-style:italic;line-height:25px;margin-top:8px}
.info ul{list-style:none;font-size:19px;line-height:24px;margin-top:18px}
.footer{right:93px;text-align:right;font-size:17px;letter-spacing:2px;color:#333;line-height:33px}
</style>
</head>
<body>

<div class="abs topbar"><span>Mobile : 0400 555 123</span><span>Fax : 08 9000 1234</span><span>P.O Box 118 Harbourside W.A 6999</span></div>

<header class="abs header">
  <div class="abs brand"><span class="brand-mark"></span><span class="brand-name">Brightvale</span></div>
  <span class="abs nav active" style="left:528px">Home</span>
  <span class="abs nav" style="left:615px">About Brightvale</span>
  <span class="abs nav" style="left:786px">Our Services</span>
  <span class="abs nav" style="left:918px">Work</span>
  <span class="abs nav" style="left:1005px">Contact</span>
</header>

<section class="abs hero" role="img" aria-label="Photograph of an empty warehouse interior with high-bay lights">
  <h1 class="abs center hero-title">We enlighten your needs.</h1>
  <p class="abs center hero-sub">Lorem ipsum dolor sit amet consectetur adipiscing elit.</p>
</section>

<section class="welcome">
  <h2 class="abs center section-title" style="top:850px">Welcome to <b>Brightvale</b>.</h2>
  <p class="abs center section-sub" style="top:892px">A professional and creative company</p>
  <div class="abs divider" style="top:951px"></div>
  <p class="abs copy" style="top:982px">Lorem ipsum dolor sit amet, consectetur adipiscing elit, sed do eiusmod tempor incididunt ut labore et dolore magna aliqua. Ut enim ad minim veniam, quis nostrud exercitation ullamco laboris nisi ut aliquip ex ea commodo consequat. Duis aute irure dolor in reprehenderit in voluptate velit esse cillum dolore eu fugiat nulla pariatur. Excepteur sint occaecat cupidatat non proident, sunt in culpa qui officia deserunt mollit anim id est laborum.</p>
  <p class="abs copy" style="top:1142px">Aipisci velit, sed quia non numquam eius modi tempora incidunt ut labore et dolore magnam aliquam quaerat voluptatem. Quis autem vel eum iure reprehenderit qui in ea voluptate velit esse quam nihil molestiae consequatur, vel illum qui dolorem eum fugiat quo voluptas nulla pariatur?</p>
</section>

<section class="abs works">
  <h2 class="abs center section-title" style="top:52px"><b>Completed</b> works</h2>
  <p class="abs center section-sub" style="top:94px">Suspendisse vel posuere lorem</p>
  <div class="abs feature" role="img" aria-label="Photograph of a municipality entry hall with ceiling downlights and seating">
    <div class="abs feature-band">
      <p class="abs feature-title">Municipality entry lighting</p>
      <p class="abs feature-date">date : February 2, 2015</p>
    </div>
  </div>
  <div class="abs thumb" style="left:105px;width:312px;background:linear-gradient(180deg,#b9b9b9 0%,#5e5e5e 45%,#8e8e8e 70%,#cfcfcf 100%)" role="img" aria-label="Black and white photograph of a completed house exterior"></div>
  <div class="abs thumb" style="left:444px;width:309px;background:linear-gradient(180deg,#4a4a4a 0%,#8a8a8a 50%,#3c3c3c 100%)" role="img" aria-label="Black and white photograph of steel reinforcement mesh on a slab"></div>
  <div class="abs thumb" style="left:780px;width:309px;background:linear-gradient(180deg,#e2e2e2 0%,#6a6a6a 40%,#4e4e4e 60%,#a8a8a8 100%)" role="img" aria-label="Black and white photograph of a row of new townhouses"></div>
</section>

<div class="abs notice"><i>Unlike others.</i> We do not disclose information to third parties.</div>

<section class="capabilities">
  <h2 class="abs center section-title" style="top:2688px"><b>Brightvale</b> Capabilities</h2>
  <p class="abs center section-sub" style="top:2730px">Magna aliqua enim minim veniam</p>
  <div class="abs divider" style="top:2784px"></div>
  <p class="abs copy" style="top:2818px">consectetur adipiscing elit, sed do eiusmod tempor incididunt ut labore et dolore magna aliqua. Ut enim ad minim veniam, quis nostrud exercitation ullamco laboris nisi ut aliquip ex ea commodo consequat. Duis aute irure dolor in reprehenderit in voluptate velit esse cillum dolore eu fugiat nulla pariatur. Excepteur sint occaecat cupidatat non proident, sunt in culpa qui officia deserunt mollit anim.</p>
  <h3 class="abs cap-head" style="top:2974px;right:618px">Commercial / Industrial</h3>
  <h3 class="abs cap-head" style="top:2974px;left:624px">Residential</h3>
  <ul class="abs cap-list cap-left" style="top:3020px">
    <li>Lighting/power design and consultation</li><li>Commercial lighting</li><li>Emergency and exit lighting</li><li>Led strip lighting</li><li>Energy efficient lighting</li><li>Temporary lighting</li><li>Illuminated signage</li><li>Switchboard relocations</li><li>Maintenance</li><li>RCD installation</li><li>Phone/data points</li><li>Data cabinets</li><li>Data Networking</li><li>IDF installations/relocations</li><li>All power requirements</li><li>All three phase power requirements</li><li>Electrical rip outs / Disconnections</li><li>Thermal imaging scans</li><li>Concrete and wall chasing</li>
  </ul>
  <ul class="abs cap-list cap-right" style="top:3020px">
    <li>RCD (Safety Switch) installat</li><li>Smoke alarms</li><li>Power points</li><li>Lighting points</li><li>External lighting</li><li>Sensor lighting</li><li>Switching</li><li>Antennas and Arial points</li><li>Dimmers</li><li>Ceiling fans</li><li>Exhaust fans</li><li>Kitchen / Bathroom Projects</li><li>Smart wiring</li><li>Phone points</li><li>Data points</li><li>Mains/sub mains cabling</li><li>Switchboard installations/relocations</li><li>Compliance investigations/inspections</li><li>Concrete and wall chasing</li>
  </ul>
  <p class="abs center support">24hr Support / faults</p>
</section>

<section class="abs contact">
  <form class="abs form-panel">
    <div class="abs field" style="top:21px">Your name</div>
    <div class="abs field" style="top:93px">Your E-mail address</div>
    <div class="abs field" style="top:162px">Your plan <small>(*if available)</small></div>
    <div class="abs upload" style="top:162px">Upload</div>
    <div class="abs field" style="top:228px;height:201px">Your message</div>
    <div class="abs send">Send now</div>
  </form>
  <div class="abs info" style="top:34px">
    <h2>Get in touch with us</h2>
    <p>Please contact Brightvale by phone numbers, the email addres form on this page for all your requirements.</p>
    <ul>
      <li>P:0400 555 123</li>
      <li>F:08 9000 1234</li>
      <li>E:info@brightvaleelectrical.com.au</li>
      <li>P.O Box 118 Harbourside W.A 6999</li>
    </ul>
  </div>
  <div class="abs footer" style="top:462px">© 2015 Brightvale. All Rights Reserved.<br>Privacy Policy | About | Contact</div>
</section>

</body>
</html>
```